Equity, Effectiveness and Efficiency in charitable food relief sector

I am undertaking my PhD in food policy in the charitable food relief sector, specifically investigating the factors (supply, demand and capacity) that affect the introduction of nutrition policy and in turn, affect the sector's ability to achieve equity, effectiveness and efficiency.

I need a graphic device that incorporates this central idea of Equity, Effectiveness and Efficiency, and how the factors of supply, demand and capacity interact. There are sub-factors within supply (1-6), demand (7-10) and capacity (11 - 15). All these details are shown in the attached figure (Basic figure_Eq Effec Effic and factors.jpg)

This figure (Basic figure_Eq Effec Effic and factors.jpg) contains all the information I need in a graphic but I need something that is more visually appealing, and that can link the ideas in a format other than a table. The final graphic will outline how the food relief sector balances the core objectives of equity, effectiveness and efficiency with the factors (and sub-factors) of supply, demand and capacity.

```html
<!DOCTYPE html>
<html lang="en">
<head>
<meta charset="utf-8">
<title>Equity – Effectiveness – Efficiency: Factors in Charitable Food Relief</title>
<link href="https://fonts.googleapis.com/css2?family=Roboto:wght@400;500;700&display=swap" rel="stylesheet">
<style>
  :root {
    --blue: #19a8e8;
    --blue-light: #3cbdf0;
    --blue-top: #16c2f3;
    --blue-deep: #0b9ddf;
    --green: #8cc63f;
    --line: #2aa9e4;
    --divider: #d9d9d9;
    --ink: #1b1b1b;
    --white: #ffffff;
  }
  * { box-sizing: border-box; margin: 0; padding: 0; }
  html, body { width: 1200px; height: 634px; overflow: hidden; background: var(--white); }
  .canvas {
    position: relative; width: 1200px; height: 634px; overflow: hidden;
    font-family: "Roboto", Arial, sans-serif; color: var(--ink);
  }
  .headline {
    position: absolute; left: 344px; top: -6px; width: 574px; height: 142px;
    background: linear-gradient(180deg, var(--blue-top), var(--blue-deep));
    border: 5px solid var(--white); border-top: none;
    border-radius: 0 0 26px 26px;
    box-shadow: 0 3px 6px rgba(0,0,0,.25);
  }
  .headline-title {
    position: absolute; left: 0; right: 0; top: 92px; text-align: center;
    color: var(--white); font-weight: 700; font-size: 25px; letter-spacing: .4px;
  }
  .headline-icons { position: absolute; left: 0; top: 0; }
  .connectors { position: absolute; left: 0; top: 0; }
  .factor-band {
    position: absolute; left: 45px; top: 235px; width: 46px; height: 360px;
    background: var(--green); border-radius: 8px;
  }
  .factor-band span {
    position: absolute; left: 50%; top: 50%;
    transform: translate(-50%, -50%) rotate(-90deg);
    white-space: nowrap; color: var(--white); font-weight: 700; font-size: 12.5px;
  }
  .divider { position: absolute; top: 264px; width: 1px; height: 331px; background: var(--divider); }
  .pill {
    position: absolute; top: 232px; width: 340px; height: 32px;
    background: var(--blue); border-radius: 7px;
  }
  .pill-label {
    position: absolute; top: 236px; color: var(--white); font-weight: 700; font-size: 19px;
  }
  .pill-badge { position: absolute; top: 216px; }
  .wheel { position: absolute; left: 0; top: 0; }
  .label {
    position: absolute; font-size: 8.6px; font-weight: 700; line-height: 1.25; color: var(--ink);
  }
  .label.end { text-align: right; }
  .label ul { list-style: none; font-weight: 400; }
</style>
</head>
<body>
<main class="canvas">

  <header class="headline">
    <svg class="headline-icons" width="574" height="100" viewBox="0 0 574 100" aria-hidden="true" fill="#fff">
      <!-- equity: three figures on steps -->
      <g transform="translate(93,40)">
        <circle cx="-14" cy="-4" r="4"/><rect x="-19" y="1" width="10" height="14" rx="2"/><rect x="-18" y="15" width="8" height="13"/>
        <circle cx="0" cy="-6" r="4"/><rect x="-5" y="-1" width="10" height="14" rx="2"/><rect x="-4" y="13" width="8" height="7"/><rect x="-6" y="21" width="12" height="7"/>
        <circle cx="14" cy="-2" r="4"/><rect x="9" y="3" width="10" height="12" rx="2"/><rect x="8" y="16" width="12" height="12"/>
      </g>
      <!-- effectiveness: gear -->
      <g transform="translate(261,50)" fill="none" stroke="#fff">
        <circle r="22" stroke-width="2" stroke-dasharray="20 8"/>
        <circle r="12" stroke-width="6" stroke-dasharray="5 3.4"/>
        <circle r="5" fill="#fff" stroke="none"/>
      </g>
      <!-- efficiency: gauge -->
      <g transform="translate(464,66)">
        <path d="M-34 0 A34 34 0 0 1 34 0 Z"/>
        <path d="M-26 -2 A26 26 0 0 1 26 -2" fill="none" stroke="#0fa8e6" stroke-width="3" stroke-dasharray="2 5"/>
        <path d="M-3 -2 L14 -20 L3 2 Z" fill="#0fa8e6"/>
        <circle r="4" fill="#0fa8e6"/>
      </g>
    </svg>
    <h1 class="headline-title">EQUITY – EFFECTIVENESS – EFFICIENCY</h1>
  </header>

  <svg class="connectors" width="1200" height="634" aria-hidden="true" fill="none" stroke="var(--line)" stroke-width="1.2">
    <path d="M628 136 V179 M265 179 H991 M265 179 V212 M628 179 V212 M991 179 V212"/>
    <path d="M261 208 L265 215 L269 208 Z M624 208 L628 215 L632 208 Z M987 208 L991 215 L995 208 Z" fill="var(--line)" stroke="none"/>
  </svg>

  <div class="factor-band"><span>Factors affecting the introduction of nutrition policy</span></div>
  <div class="divider" style="left:445px"></div>
  <div class="divider" style="left:809px"></div>

  <!-- section headers -->
  <div class="pill" style="left:95px"></div>
  <div class="pill" style="left:459px"></div>
  <div class="pill" style="left:821px"></div>
  <svg class="pill-badge" style="left:158px" width="60" height="64" aria-hidden="true">
    <circle cx="30" cy="32" r="29" fill="#fff"/><circle cx="30" cy="32" r="24" fill="var(--green)"/>
    <g fill="#fff"><rect x="19" y="27" width="10" height="9"/><rect x="31" y="27" width="10" height="9"/><rect x="25" y="17" width="10" height="9"/><rect x="16" y="38" width="28" height="3"/><rect x="18" y="42" width="3" height="4"/><rect x="39" y="42" width="3" height="4"/></g>
  </svg>
  <svg class="pill-badge" style="left:559px" width="60" height="64" aria-hidden="true">
    <circle cx="30" cy="32" r="29" fill="#fff"/><circle cx="30" cy="32" r="24" fill="var(--green)"/>
    <path d="M17 16 V46 H45" fill="none" stroke="#fff" stroke-width="2"/>
    <path d="M20 24 L27 32 L32 28 L41 40" fill="none" stroke="#fff" stroke-width="2"/>
    <rect x="31" y="14" width="10" height="10" rx="1" fill="#fff"/>
  </svg>
  <svg class="pill-badge" style="left:921px" width="60" height="64" aria-hidden="true">
    <circle cx="30" cy="32" r="29" fill="#fff"/><circle cx="30" cy="32" r="24" fill="var(--green)"/>
    <path d="M16 26 L30 16 L44 26 V46 H16 Z" fill="#fff"/>
    <rect x="22" y="32" width="16" height="14" fill="var(--green)"/>
    <rect x="24" y="38" width="5" height="6" fill="#fff"/><rect x="31" y="38" width="5" height="6" fill="#fff"/>
  </svg>
  <h2 class="pill-label" style="left:235px">Supply</h2>
  <h2 class="pill-label" style="left:636px">Demand</h2>
  <h2 class="pill-label" style="left:998px">Capacity</h2>

  <!-- factor wheels -->
  <svg class="wheel" width="1200" height="634" aria-label="Sub-factor wheels for supply, demand and capacity" fill="none" stroke-width="35">
    <g>
      <circle cx="265" cy="414" r="67.5" pathLength="360" stroke="var(--blue)"  stroke-dasharray="58 302" transform="rotate(-89 265 414)"/>
      <circle cx="265" cy="414" r="67.5" pathLength="360" stroke="var(--green)" stroke-dasharray="58 302" transform="rotate(-29 265 414)"/>
      <circle cx="265" cy="414" r="67.5" pathLength="360" stroke="var(--blue)"  stroke-dasharray="58 302" transform="rotate(31 265 414)"/>
      <circle cx="265" cy="414" r="67.5" pathLength="360" stroke="var(--green)" stroke-dasharray="58 302" transform="rotate(91 265 414)"/>
      <circle cx="265" cy="414" r="67.5" pathLength="360" stroke="var(--blue)"  stroke-dasharray="58 302" transform="rotate(151 265 414)"/>
      <circle cx="265" cy="414" r="67.5" pathLength="360" stroke="var(--green)" stroke-dasharray="58 302" transform="rotate(211 265 414)"/>
      <circle cx="265" cy="414" r="54" stroke="#fff" stroke-opacity=".22" stroke-width="8"/>
    </g>
    <g>
      <circle cx="628" cy="414" r="67.5" pathLength="360" stroke="var(--blue)"  stroke-dasharray="88 272" transform="rotate(-89 628 414)"/>
      <circle cx="628" cy="414" r="67.5" pathLength="360" stroke="var(--green)" stroke-dasharray="88 272" transform="rotate(1 628 414)"/>
      <circle cx="628" cy="414" r="67.5" pathLength="360" stroke="var(--blue)"  stroke-dasharray="88 272" transform="rotate(91 628 414)"/>
      <circle cx="628" cy="414" r="67.5" pathLength="360" stroke="var(--green)" stroke-dasharray="88 272" transform="rotate(181 628 414)"/>
      <circle cx="628" cy="414" r="54" stroke="#fff" stroke-opacity=".22" stroke-width="8"/>
    </g>
    <g>
      <circle cx="991" cy="414" r="67.5" pathLength="360" stroke="var(--blue)"       stroke-dasharray="70 290" transform="rotate(-89 991 414)"/>
      <circle cx="991" cy="414" r="67.5" pathLength="360" stroke="var(--green)"      stroke-dasharray="70 290" transform="rotate(-17 991 414)"/>
      <circle cx="991" cy="414" r="67.5" pathLength="360" stroke="var(--blue)"       stroke-dasharray="70 290" transform="rotate(55 991 414)"/>
      <circle cx="991" cy="414" r="67.5" pathLength="360" stroke="var(--green)"      stroke-dasharray="70 290" transform="rotate(127 991 414)"/>
      <circle cx="991" cy="414" r="67.5" pathLength="360" stroke="var(--blue-light)" stroke-dasharray="70 290" transform="rotate(199 991 414)"/>
      <circle cx="991" cy="414" r="54" stroke="#fff" stroke-opacity=".22" stroke-width="8"/>
    </g>

    <!-- small segment icons -->
    <g fill="#fff" stroke="none">
      <g transform="translate(299,356)"><rect x="-7" y="-3" width="6" height="5"/><rect x="1" y="-3" width="6" height="5"/><rect x="-3" y="-9" width="6" height="5"/><rect x="-8" y="3" width="16" height="2"/></g>
      <g transform="translate(332,414)"><text x="2" y="-1" font-size="11" font-weight="700" font-family="Roboto, Arial, sans-serif">$</text><path d="M-9 3 Q-2 0 4 5 L8 2 L9 4 L3 9 Z"/></g>
      <g transform="translate(299,472)"><circle r="7" fill="none" stroke="#fff" stroke-width="1.6"/><path d="M0 -4 V0 H3" stroke="#fff" stroke-width="1.4" fill="none"/></g>
      <g transform="translate(231,472)"><rect x="-8" y="-2" width="7" height="8"/><rect x="1" y="-6" width="7" height="12"/><circle cx="-2" cy="-7" r="2"/></g>
      <g transform="translate(198,414)"><rect x="-3" y="-9" width="8" height="7"/><path d="M-9 2 Q-2 -1 4 3 L8 1 L9 3 L3 8 Z"/></g>
      <g transform="translate(231,356)"><path d="M-9 1 L-4 -4 L0 -1 L4 -4 L9 1 L3 6 Z"/></g>

      <g transform="translate(676,366)"><path d="M-7 -7 V7 H8" stroke="#fff" stroke-width="1.4" fill="none"/><path d="M-5 -3 L-1 2 L3 -1 L7 5" stroke="#fff" stroke-width="1.4" fill="none"/><rect x="1" y="-9" width="6" height="6"/></g>
      <g transform="translate(676,462)"><path d="M-7 -7 V7 H8" stroke="#fff" stroke-width="1.4" fill="none"/><path d="M-5 0 L-1 4 L3 1 L7 6" stroke="#fff" stroke-width="1.4" fill="none"/><ellipse cx="3" cy="-5" rx="5" ry="3"/></g>
      <g transform="translate(580,462)"><circle cx="-6" cy="0" r="5" fill="none" stroke="#fff" stroke-width="1.4"/><circle cx="6" cy="0" r="5"/></g>
      <g transform="translate(580,366)"><path d="M-6 -3 H6 L4 8 H-4 Z"/><rect x="-7" y="-6" width="14" height="2"/><circle cx="3" cy="-9" r="2"/></g>

      <g transform="translate(1031,359)"><path d="M-8 -2 L0 -8 L8 -2 V8 H-8 Z"/></g>
      <g transform="translate(1055,435)"><rect x="-9" y="-5" width="11" height="9"/><path d="M3 -2 H7 L9 1 V4 H3 Z"/><circle cx="-5" cy="6" r="2"/><circle cx="5" cy="6" r="2"/></g>
      <g transform="translate(991,481)"><circle cy="-3" r="3"/><path d="M-5 5 Q0 -1 5 5 Z"/><circle cx="-8" cy="7" r="2"/><circle cx="8" cy="7" r="2"/></g>
      <g transform="translate(927,435)"><circle cx="-5" cy="-5" r="3"/><circle cx="5" cy="-5" r="3"/><circle cx="-5" cy="5" r="3"/><circle cx="5" cy="5" r="3"/></g>
      <g transform="translate(951,359)"><circle cx="-3" cy="1" r="6"/><rect x="3" y="-3" width="7" height="10"/></g>
    </g>
  </svg>

  <!-- supply labels -->
  <p class="label end" style="right:993px;top:322px">Donor<br>relationships</p>
  <p class="label" style="left:320px;top:322px">Uncertain<br>material supply</p>
  <p class="label" style="left:355px;top:409px">Uncertain<br>Monetary supply</p>
  <p class="label" style="left:323px;top:492px">Limited food supply</p>
  <p class="label end" style="right:992px;top:492px">Perish ability</p>
  <p class="label end" style="right:1025px;top:409px">Donor<br>constraints</p>

  <!-- demand labels -->
  <p class="label end" style="right:645px;top:338px">Food<br>wastage</p>
  <p class="label" style="left:701px;top:338px">Uncertain<br>demand</p>
  <p class="label" style="left:703px;top:472px">Limited demand<br>visibility</p>
  <p class="label end" style="right:647px;top:472px">Client<br>choice</p>

  <!-- capacity labels -->
  <p class="label end" style="right:272px;top:333px">Budget</p>
  <div class="label" style="left:1052px;top:311px">Storage
    <ul><li>- Cold</li><li>- Warehouse</li></ul></div>
  <p class="label" style="left:1081px;top:438px">Transportation</p>
  <div class="label end" style="right:300px;top:433px">External<br>stakeholders</div>
  <div class="label" style="left:963px;top:508px">Workforce
    <ul><li>- Volunteers</li><li>- Expertise and training</li><li>- Attitudes and Beliefs</li><li>- Collaboration</li><li>- Executive Support</li></ul></div>

</main>
</body>
</html>
```